Titleway Settlement Group

We are a legal service provider.
We deal predominately with Real Estate title transfers.
We will be printing on white paper with black ink, so colour is not really needed for the letter head.

I have enclosed our logo which i will like to be incorporated into the letterhead.

I have also attached a copy of our current old letterhead with all our office details on there. Everything that is listed in the current letterhead i would like to be included in the new one.

Target Market(s)

Real Estate, Home buyers & Sellers, Solicitors and Lawyers, Pest & Building Inspectors

Industry/Entity Type

Legal

Font styles to use
Serif

Requirements
Must have
• Simple and Legal looking.

```html
<!DOCTYPE html>
<html lang="en">
<head>
<meta charset="utf-8">
<title>Titleway Settlement Group Letterhead</title>
<link href="https://fonts.googleapis.com/css2?family=Tinos:wght@400;700&display=swap" rel="stylesheet">
<style>
  :root {
    --ink: #222222;
    --ink-soft: #444444;
    --swoosh-dark: #2b2b2b;
    --swoosh-mid: #8a8a8a;
    --swoosh-light: #d4d4d4;
    --paper: #ffffff;
    --rule: #555555;
  }
  * { margin: 0; padding: 0; box-sizing: border-box; }
  html, body { width: 849px; height: 1200px; overflow: hidden; background: var(--paper); }
  .letterhead {
    position: relative;
    width: 849px;
    height: 1200px;
    background: var(--paper);
    font-family: "Tinos", "Times New Roman", serif;
    color: var(--ink);
    overflow: hidden;
  }
  .page-curves { position: absolute; inset: 0; width: 849px; height: 1200px; }

  .brand {
    position: absolute;
    top: 100px;
    left: 0;
    width: 849px;
    display: flex;
    justify-content: center;
    align-items: center;
    gap: 14px;
  }
  .brand-mark { width: 30px; height: 30px; background: var(--ink); }
  .brand-name {
    font-size: 40px;
    font-weight: 700;
    letter-spacing: 1px;
    color: var(--ink);
  }

  .credentials {
    position: absolute;
    top: 196px;
    left: 0;
    width: 849px;
    text-align: center;
    line-height: 1.15;
  }
  .credentials-title { font-size: 24px; letter-spacing: 0.5px; }
  .credentials-line { font-size: 20px; }

  .footer-rule {
    position: absolute;
    top: 1026px;
    left: 32px;
    width: 790px;
    border-top: 1.5px solid var(--rule);
  }
  .membership {
    position: absolute;
    top: 1040px;
    left: 140px;
    width: 560px;
    text-align: center;
    font-size: 12px;
    line-height: 1.45;
    color: var(--ink-soft);
  }
  .office-address {
    position: absolute;
    top: 1090px;
    left: 140px;
    width: 560px;
    text-align: center;
    font-size: 12px;
    color: var(--ink-soft);
  }
  .contact-numbers, .correspondence {
    position: absolute;
    top: 1122px;
    font-size: 12px;
    line-height: 1.4;
    color: var(--ink-soft);
  }
  .contact-numbers { left: 58px; }
  .correspondence { left: 424px; }
  .contact-numbers span.label { display: inline-block; width: 56px; }
</style>
</head>
<body>
<div class="letterhead">
  <svg class="page-curves" viewBox="0 0 849 1200" aria-hidden="true">
    <!-- top-left corner swoosh -->
    <path d="M0 0 H260 C150 20 50 120 0 330 Z" fill="var(--swoosh-dark)"/>
    <path d="M0 330 C50 120 150 20 260 0 H300 C170 30 60 140 0 400 Z" fill="var(--swoosh-light)"/>
    <!-- right edge sweep -->
    <path d="M790 0 C840 180 845 500 849 700 V0 Z" fill="var(--swoosh-light)"/>
    <path d="M810 0 C845 150 849 400 849 520 V0 Z" fill="var(--swoosh-mid)"/>
    <!-- left edge thin arc -->
    <path d="M0 420 C14 600 20 800 30 1010" fill="none" stroke="var(--swoosh-light)" stroke-width="6"/>
    <!-- bottom-right swoosh -->
    <path d="M849 860 C830 960 760 1010 640 1026 H849 Z" fill="var(--swoosh-light)"/>
    <path d="M849 900 C835 975 780 1012 700 1026 H849 Z" fill="var(--swoosh-mid)"/>
    <path d="M849 950 C840 990 810 1015 770 1026 H849 Z" fill="var(--swoosh-dark)"/>
    <!-- bottom-left base -->
    <path d="M0 1200 C200 1185 500 1180 849 1170 V1200 Z" fill="var(--swoosh-light)"/>
  </svg>

  <header class="brand">
    <div class="brand-mark"></div>
    <div class="brand-name">TITLEWAY SETTLEMENT GROUP</div>
  </header>

  <section class="credentials">
    <p class="credentials-title">CERTIFIED PRACTISING CONVEYANCERS</p>
    <p class="credentials-line">Licensee: Helena Maris Doukas</p>
    <p class="credentials-line">Certified Practising Conveyancer: 204718</p>
  </section>

  <div class="footer-rule"></div>

  <footer>
    <div class="membership">
      <p>Member of the Association of Property Conveyancers</p>
      <p>A.B.N. 48 902 315 274</p>
    </div>
    <p class="office-address">Shop 4, 12-16 Harbour Road, (Cnr Elm Street) KOGARAH NSW 2217</p>
    <div class="contact-numbers">
      <p><span class="label">Phone:</span>02 9000 4812</p>
      <p><span class="label">Fax:</span>02 9000 4813</p>
      <p><span class="label">Mobile:</span>0400 555 019</p>
    </div>
    <div class="correspondence">
      <p>All Correspondence to:</p>
      <p>P.O. Box 1207 Carlton NSW 2218</p>
      <p>Email: helena_doukas@examplemail.com.au</p>
    </div>
  </footer>
</div>
</body>
</html>
```